Business Card & Stationary
For Event Planning Website
I need single sided standard sized Business Card [3.5" x 2"]
Same as logo or similar
Professional
First Name Last Name
Founder & Chief Executive Officer
Address 1
Address 2
New York, NY 10016
xyz@juniperhours.com
www.juniperhours.com
Feel free to be creative - the site is for party planning (weddings, bar-mitzvahs, etc.) so it should be modern & professional, with a fun factor.
I used test data to protect personal data but I can supply you with all of the information you need later.
I'm not sure which eps file corresponds to the jpg.
This is the hamsa (hand) which is part of the logo
The hand - ai file
Webpage Background Pattern

```html
<!DOCTYPE html>
<html lang="en">
<head>
<meta charset="utf-8">
<title>JuniperHours — Business Card</title>
<link rel="stylesheet" href="https://fonts.googleapis.com/css2?family=Arimo:wght@400&display=swap">
<style>
  :root {
    --card-top: #ffffff;
    --card-bottom: #d9e4f3;
    --pattern-tone: #c9d8ee;
    --brand-blue: #1b70b8;
    --text-blue: #1d4f9c;
    --band-blue: #1e63ad;
    --band-text: #ffffff;
  }
  html, body {
    margin: 0;
    padding: 0;
    overflow: hidden;
    background: #ffffff;
  }
  .card {
    position: relative;
    width: 1200px;
    height: 686px;
    overflow: hidden;
    font-family: "Arimo", Arial, sans-serif;
  }
  .card-background {
    position: absolute;
    inset: 0;
    background:
      radial-gradient(ellipse at 30% 10%, rgba(255,255,255,0.9), rgba(255,255,255,0) 60%),
      linear-gradient(180deg, var(--card-top) 0%, var(--card-bottom) 100%);
  }
  .holder {
    position: absolute;
    left: 43px;
    top: 88px;
    color: var(--brand-blue);
    font-size: 28px;
    line-height: 43px;
  }
  .holder p { margin: 0; }
  .wordmark {
    position: absolute;
    left: 40px;
    top: 300px;
    margin: 0;
    color: var(--brand-blue);
    font-size: 84px;
    font-weight: 400;
    letter-spacing: -1px;
    line-height: 1;
  }
  .wordmark-dot {
    position: absolute;
    left: 610px;
    top: 398px;
    width: 52px;
    height: 52px;
    border-radius: 50%;
    background: var(--brand-blue);
  }
  .divider {
    position: absolute;
    left: 706px;
    top: 228px;
    width: 3px;
    height: 312px;
    background: var(--band-blue);
  }
  .contact {
    position: absolute;
    left: 732px;
    top: 258px;
    color: var(--text-blue);
    font-size: 25px;
    line-height: 36px;
    font-style: normal;
  }
  .contact p { margin: 0; }
  .contact .phone { margin-top: 22px; }
  .contact .email { margin-top: 30px; }
  .web-band {
    position: absolute;
    left: 0;
    bottom: 0;
    width: 100%;
    height: 43px;
    background: var(--band-blue);
    color: var(--band-text);
    font-size: 25px;
    line-height: 43px;
    text-align: center;
  }
</style>
</head>
<body>
  <main class="card">
    <div class="card-background" role="img" aria-label="Soft pale-blue background with a faint repeating circle pattern"></div>

    <section class="holder">
      <p class="holder-name">First Name Last Name</p>
      <p class="holder-title">Founder &amp; Chief Executive Office</p>
    </section>

    <h1 class="wordmark">juniperhours</h1>
    <span class="wordmark-dot" aria-hidden="true"></span>

    <div class="divider" aria-hidden="true"></div>

    <address class="contact">
      <p>Address&nbsp; Address 1</p>
      <p>Address 2</p>
      <p>New York, NY 10016</p>
      <p class="phone">Phone : (212) 555-1212</p>
      <p class="email">Email : xyz@juniperhours.com</p>
    </address>

    <footer class="web-band">www.juniperhours.com</footer>
  </main>
</body>
</html>
```